a two sided flyer to advertise osteopathic/pilates business

we need a square format flyer that introduces our pilates business on one sided and our osteopathic business on the other.
we want the look an feel to be in rough keeping with some work we had done a while go and can be attached.

kelb osteopathy
BEAT PAIN
sports/spinal/pre+post natal
kelbclinic.com.au
94620381

kelb pilates
movement + strength
3 classes - $45
kelbclinic.com.au
94620381

Requirements
Must have
• 2 sided, consisten look and feel and a look and feel consistent with the kelb pilates png files attached
• charcoal/orange/white as a colour scheme

```html
<!DOCTYPE html>
<html lang="en">
<head>
<meta charset="utf-8">
<title>kelb osteopathy &amp; kelb pilates flyer</title>
<link rel="stylesheet" href="https://fonts.googleapis.com/css2?family=Exo+2:wght@500;600;700&family=Oswald:wght@400&display=swap">
<style>
  :root {
    --charcoal: #231f20;
    --orange: #f7941d;
    --orange-deep: #f58a1f;
    --peach: #fde6d0;
    --white: #ffffff;
    --silver: #d9d9d9;
  }
  * { margin: 0; padding: 0; box-sizing: border-box; }
  html, body { width: 1200px; height: 1200px; overflow: hidden; background: var(--white); }
  body { position: relative; font-family: "Exo 2", sans-serif; }

  .flyer-side { position: absolute; width: 552px; height: 552px; overflow: hidden; }

  /* Osteopathy side */
  .osteo-side { left: 60px; top: 70px; background: var(--orange); }
  .osteo-side .side-shape { position: absolute; inset: 0; }
  .osteo-brand { position: absolute; left: 36px; top: 30px; display: flex; align-items: center; gap: 22px; }
  .brand-circle { width: 90px; height: 90px; border-radius: 50%; background: var(--orange); display: flex; align-items: center; justify-content: center; color: var(--white); font-weight: 700; font-size: 30px; }
  .brand-services { font-family: "Oswald", sans-serif; color: var(--white); font-size: 23px; line-height: 1.05; letter-spacing: 0.2px; }
  .osteo-copy { position: absolute; left: 26px; top: 258px; color: var(--white); }
  .osteo-name { font-weight: 600; font-size: 38px; line-height: 1; }
  .osteo-headline { font-family: Arial, "Helvetica", sans-serif; font-weight: 700; font-size: 55px; line-height: 1.05; margin-top: 6px; margin-left: -2px; }
  .osteo-services { font-weight: 600; font-size: 18.5px; margin-top: 8px; }
  .osteo-contact { position: absolute; left: 28px; top: 433px; color: var(--white); font-weight: 600; font-size: 34px; line-height: 1.42; }

  /* Pilates side */
  .pilates-side { left: 590px; top: 578px; background: linear-gradient(180deg, var(--peach) 0%, #fcd4a8 45%, var(--orange) 82%, var(--orange-deep) 100%); }
  .movement-art { position: absolute; left: 28px; top: 28px; width: 246px; height: 296px; background: radial-gradient(ellipse at center, rgba(247,148,29,0.55), rgba(247,148,29,0.15) 70%, rgba(247,148,29,0) 100%); border-radius: 10px; }
  .pilates-brand { position: absolute; left: 316px; top: 40px; width: 204px; height: 204px; border-radius: 50%; background: var(--charcoal); display: flex; align-items: center; justify-content: center; color: var(--white); font-weight: 700; font-size: 54px; }
  .pilates-offer { position: absolute; right: 34px; top: 262px; text-align: right; color: var(--charcoal); font-weight: 700; font-size: 38px; line-height: 1.5; }
  .pilates-contact { position: absolute; left: 26px; top: 446px; color: var(--white); font-weight: 600; font-size: 34px; line-height: 1.42; }
</style>
</head>
<body>
  <section class="flyer-side osteo-side">
    <svg class="side-shape" viewBox="0 0 552 552" width="552" height="552" aria-hidden="true">
      <defs>
        <linearGradient id="swoosh-fill" x1="0" y1="0" x2="1" y2="0">
          <stop offset="0" stop-color="#9a9a9a"/>
          <stop offset="0.45" stop-color="#f4f4f4"/>
          <stop offset="1" stop-color="#ffffff"/>
        </linearGradient>
      </defs>
      <path d="M380 0 H430 C520 110 520 220 470 320 C430 400 440 480 500 552 H420 C370 470 360 390 400 300 C440 200 440 100 380 0 Z" fill="url(#swoosh-fill)"/>
      <path d="M0 0 H380 C440 100 440 200 400 300 C360 390 370 470 420 552 H0 Z" fill="var(--charcoal)"/>
    </svg>
    <div class="osteo-brand">
      <div class="brand-circle">kelb</div>
      <div class="brand-services">OSTEOPATHY<br>CLINICAL PILATES</div>
    </div>
    <div class="osteo-copy">
      <p class="osteo-name">kelb osteopathy</p>
      <p class="osteo-headline">BEAT PAIN</p>
      <p class="osteo-services">sports/spinal/pre+post natal</p>
    </div>
    <p class="osteo-contact">kelbclinic.com.au<br>94620381</p>
  </section>

  <section class="flyer-side pilates-side">
    <div class="movement-art" role="img" aria-label="Orange silhouettes of people in pilates and stretching poses"></div>
    <div class="pilates-brand">kelb</div>
    <div class="pilates-offer">
      <p>kelb pilates</p>
      <p>movement + strength</p>
      <p>3 classes - $45</p>
    </div>
    <p class="pilates-contact">kelbclinic.com.au<br>94620381</p>
  </section>
</body>
</html>
```